Business card for our large format printing and installation business

We want a professional looking business card for our business. We manufacture and install Signs.

On the back of the card add this info
Large Format Graphics Printing & Installations, Event Graphics, Banners, Posters, Vehicle Fleet Graphics, Boat Wraps, Wall Murals, Decals,Displays,Signs,Plaques,Digital Signs

On the Front of the card add the Tallowfern Signs logo, plus On the back of the card add the Orange Tallowfern Wraps logo. The 2 vector logos are attached to the design brief.

Target Market(s)

Local business owners

Contact Information for Business Card

Colors
f37122
f68d4e
f9ba93

Requirements
Must have
• On the Front of the card add the Tallowfern Signs logo, plus On the back of the card add the Orange Tallowfern Wraps logo. The 2 vector logos are attached to the design brief.

```html
<!DOCTYPE html>
<html lang="en">
<head>
<meta charset="utf-8">
<title>Tallowfern Signs – Business Card</title>
<link href="https://fonts.googleapis.com/css2?family=Arimo:wght@400;700&display=swap" rel="stylesheet">
<style>
  :root {
    --stage: #2b2b2b;
    --card: #232323;
    --ink: #f2f2f2;
    --accent: #f7a21b;
    --accent-deep: #f37122;
    --accent-bright: #ffd21a;
    --rule: #9a9a9a;
  }
  * { margin: 0; padding: 0; box-sizing: border-box; }
  html, body {
    width: 1200px; height: 895px; overflow: hidden;
    background: var(--stage);
    font-family: "Arimo", Arial, sans-serif;
  }
  .canvas { position: relative; width: 1200px; height: 895px; }
  .card {
    position: absolute;
    width: 640px; height: 366px;
    background: var(--card);
    border-radius: 14px;
    overflow: hidden;
    box-shadow: 0 14px 30px rgba(0,0,0,.55);
  }
  .card::after {
    content: ""; position: absolute; left: 0; right: 0; bottom: 0; height: 4px;
    background: linear-gradient(90deg, var(--accent-deep), var(--accent-bright));
  }
  .card--front { left: 60px; top: 64px; }
  .card--back { left: 500px; top: 470px; }

  .brand-name {
    font-weight: 700; color: var(--accent);
    white-space: nowrap; letter-spacing: .5px;
  }
  .card--front .brand-name {
    position: absolute; left: 0; right: 0; top: 130px;
    text-align: center; font-size: 52px;
  }
  .card--front .site {
    position: absolute; right: 70px; bottom: 46px;
    color: var(--ink); font-size: 17px;
  }

  .card--back .brand-name {
    position: absolute; right: 40px; top: 40px; font-size: 32px;
  }
  .contact-block {
    position: absolute; left: 56px; top: 170px;
  }
  .identity {
    border-left: 1px solid var(--rule);
    padding-left: 18px; margin-bottom: 18px;
  }
  .person-name { color: var(--accent); font-weight: 700; font-size: 25px; letter-spacing: .5px; }
  .person-role { color: var(--ink); font-size: 20px; margin-top: 2px; }
  .contact-list { list-style: none; }
  .contact-list li {
    display: flex; align-items: center; gap: 10px;
    color: var(--ink); font-size: 17px; line-height: 24px;
  }
  .contact-list svg { width: 15px; height: 15px; fill: var(--accent); flex: none; }
  .address {
    position: absolute; right: 40px; top: 200px;
    text-align: right; color: var(--ink); font-size: 18px; line-height: 23px;
  }
</style>
</head>
<body>
<main class="canvas">
  <section class="card card--front" aria-label="Card front">
    <div class="brand-name">Tallowfern Signs</div>
    <div class="site">www.tallowfernwraps.com</div>
  </section>

  <section class="card card--back" aria-label="Card back">
    <div class="brand-name">Tallowfern Signs</div>

    <div class="contact-block">
      <div class="identity">
        <div class="person-name">MARCO DELVANE</div>
        <div class="person-role">CEO</div>
      </div>
      <ul class="contact-list">
        <li><svg viewBox="0 0 24 24"><path d="M6.6 10.8a15 15 0 0 0 6.6 6.6l2.2-2.2a1 1 0 0 1 1-.25 11.4 11.4 0 0 0 3.6.57 1 1 0 0 1 1 1V20a1 1 0 0 1-1 1A17 17 0 0 1 3 4a1 1 0 0 1 1-1h3.5a1 1 0 0 1 1 1c0 1.25.2 2.45.57 3.57a1 1 0 0 1-.25 1z"/></svg>555-204-1187 (direct)</li>
        <li><svg viewBox="0 0 24 24"><path d="M2 8c3-4 17-4 20 0l-1 3h-4l-1-2H8l-1 2H3zM5 12h14l2 8H3zm7 2a2.5 2.5 0 1 0 0 5 2.5 2.5 0 0 0 0-5z"/></svg>555-318-6402</li>
        <li><svg viewBox="0 0 24 24"><path d="M2 5h20v14H2zm2 2v.5l8 5 8-5V7l-8 5z"/></svg>marco@tallowfern.net</li>
        <li><svg viewBox="0 0 24 24"><path d="M12 2a10 10 0 1 0 0 20 10 10 0 0 0 0-20zm0 2c.9 0 2 1.6 2.5 4h-5C10 5.6 11.1 4 12 4zM4.5 10h3.2a17 17 0 0 0 0 4H4.5a8 8 0 0 1 0-4zm5.2 0h4.6a15 15 0 0 1 0 4H9.7a15 15 0 0 1 0-4zm6.6 0h3.2a8 8 0 0 1 0 4h-3.2a17 17 0 0 0 0-4zM9.5 16h5c-.5 2.4-1.6 4-2.5 4s-2-1.6-2.5-4z"/></svg>www.tallowfernwraps.com</li>
      </ul>
    </div>

    <address class="address" style="font-style:normal">
      1840 Harbor Mill Road #4<br>
      Crestmoor Bay<br>
      FL 34517
    </address>
  </section>
</main>
</body>
</html>
```